Baby Boutique Needs a Business Card Design

We need a modern double sided business card design using the attached logo for Lil' Tot Nook.

Lil' Tot Nook is a baby boutique which sells only handmade clothing and accessories for both boys and girls. Our store will live exclusively online.

We would like to only use the colors that have been used in the logo.

Target Market(s)

Potential wholesale clients, Small business owners

Industry/Entity Type

Retail

Contact Information for Business Card

Name Wendell J. Ferris (Owner)
Email sales@ltotnook.com
Main Phone 787-203-6159
Cell phone 787-203-6742
Website www.LTotNook.com

Font styles to use
Sans Serif

Colors

Designer to choose colors to be used in the design.

Requirements
Must have
• -Would like to have icons that indentify the contact information.
• -Include our website
• -Include our tagline in a small area near the bottom. "Handmade Baby Creations"
• -Would like to include Facebook and Instagram Icons
• -
Nice to have
• Would like to have a simple back side with the logo.
• Something along the lines of the harbor ledger card attached.

```html
<!DOCTYPE html>
<html lang="en">
<head>
<meta charset="utf-8">
<title>Lil' Tot Nook – Business Card</title>
<link rel="stylesheet" href="https://fonts.googleapis.com/css2?family=Arimo:wght@400;700&family=Montserrat:wght@700&display=swap">
<style>
  :root {
    --stage: #2b2b2c;
    --card: #1f2326;
    --teal: #6fc9b6;
    --coral: #e0625c;
    --social-a: #3b5a98;
    --social-b: #2e6d9a;
  }
  * { margin: 0; padding: 0; box-sizing: border-box; }
  html, body { width: 1200px; height: 1189px; overflow: hidden; }
  body {
    background: var(--stage);
    font-family: "Arimo", Arial, sans-serif;
    position: relative;
  }
  .card {
    position: absolute;
    left: 180px;
    width: 840px;
    height: 480px;
    background: var(--card);
    border-radius: 26px;
    box-shadow: 0 18px 40px rgba(0,0,0,.45);
  }
  .card--back { top: 74px; }
  .card--front { top: 634px; }

  .wordmark {
    font-family: "Arimo", Arial, sans-serif;
    font-weight: 700;
    color: var(--teal);
    line-height: 1;
    white-space: nowrap;
  }

  /* back side */
  .card--back .wordmark {
    position: absolute;
    left: 0; right: 0;
    top: 150px;
    text-align: center;
    font-size: 72px;
  }
  .social {
    position: absolute;
    top: 262px;
    left: 0; right: 0;
    display: flex;
    justify-content: center;
    gap: 12px;
  }
  .social__item { width: 34px; height: 34px; border-radius: 3px; }
  .social__item--one { background: var(--social-a); }
  .social__item--two { background: var(--social-b); }
  .card--back .website {
    position: absolute;
    left: 0; right: 0;
    top: 322px;
    text-align: center;
    color: var(--teal);
    font-size: 20px;
    letter-spacing: 5px;
  }

  /* front side */
  .card--front .wordmark {
    position: absolute;
    left: 60px;
    top: 196px;
    font-size: 50px;
  }
  .divider {
    position: absolute;
    left: 470px;
    top: 110px;
    width: 2px;
    height: 180px;
    background: var(--teal);
  }
  .contact {
    position: absolute;
    left: 510px;
    top: 108px;
  }
  .contact__name {
    font-family: "Montserrat", Arial, sans-serif;
    font-size: 24px;
    color: var(--teal);
  }
  .contact__role {
    font-size: 19px;
    color: var(--coral);
    margin-bottom: 12px;
  }
  .contact__list { list-style: none; }
  .contact__item {
    display: flex;
    align-items: center;
    gap: 12px;
    font-size: 20px;
    color: var(--teal);
    line-height: 27px;
  }
  .contact__icon { width: 18px; height: 18px; flex: none; }
  .tagline {
    position: absolute;
    left: 0; right: 0;
    bottom: 58px;
    text-align: center;
    color: var(--teal);
    font-size: 22px;
    letter-spacing: 7px;
  }
</style>
</head>
<body>

<section class="card card--back" aria-label="Card back">
  <div class="wordmark">Lil' Tot Nook</div>
  <div class="social" aria-label="Social profiles">
    <span class="social__item social__item--one"></span>
    <span class="social__item social__item--two"></span>
  </div>
  <div class="website">www.LTotNook.com</div>
</section>

<section class="card card--front" aria-label="Card front">
  <div class="wordmark">Lil' Tot Nook</div>
  <div class="divider"></div>
  <div class="contact">
    <div class="contact__name">Wendell J. Ferris</div>
    <div class="contact__role">Owner</div>
    <ul class="contact__list">
      <li class="contact__item">
        <svg class="contact__icon" viewBox="0 0 20 20" aria-hidden="true"><path fill="var(--coral)" d="M2 8c0-3 4-5 8-5s8 2 8 5v1h-4V7H6v2H2zM5 10h10l2 7H3z"/></svg>
        787-203-6159
      </li>
      <li class="contact__item">
        <svg class="contact__icon" viewBox="0 0 20 20" aria-hidden="true"><rect x="5" y="1.5" width="10" height="17" rx="2" fill="none" stroke="var(--coral)" stroke-width="2"/></svg>
        787-203-6742
      </li>
      <li class="contact__item">
        <svg class="contact__icon" viewBox="0 0 20 20" aria-hidden="true"><rect x="1" y="4" width="18" height="12" fill="var(--coral)"/><path d="M1 4l9 7 9-7" fill="none" stroke="var(--card)" stroke-width="1.5"/></svg>
        sales@ltotnook.com
      </li>
      <li class="contact__item">
        <svg class="contact__icon" viewBox="0 0 20 20" aria-hidden="true"><g fill="none" stroke="var(--coral)" stroke-width="1.6"><circle cx="10" cy="10" r="8"/><ellipse cx="10" cy="10" rx="3.5" ry="8"/><path d="M2 10h16M4 5.5h12M4 14.5h12"/></g></svg>
        www.LTotNook.com
      </li>
    </ul>
  </div>
  <div class="tagline">Handmade Baby Creations</div>
</section>

</body>
</html>
```